Logo & Visitenkarte für Schreinermonteur (Fenster und Türen)
Sehr gute Designerin, gute Ideen und sie hat alle Änderungswünsche sehr schnell und genau umgesetzt. Jederzeit gerne wieder!
Zielgruppe
Verkauf und Einbau von Fenster und Türen (Bauelemente). Meine Zielgruppen sind Menschen, die ein Haus bauen oder renovieren und Fenster und Türen benötigen. Ich mache die Berautung und baue anschliessend die Türen, Fenster und Jalousien auch mit meinem Team ein.
Aufgabenstellung
Ich bin selbständiger Schreiner im Südschwarzwald und derzeit auf den Einbau von Fenster und Türen spezialisiert. Ich möchte meine Initialien KM in meinem Logo enthalten haben, bin aber auch offen für andere Vorschläge. Derzeit bin ich unter 'KM Holzmontagen' bekannt.
Gerne darf als Untertitel 'Fenster und Türen' verwendet werden. Da ich die Option haben möchte, dass ich das Logo/meine Initialien weiterverwende, aber meine Spezialisierung von 'Fenster und Türen' ändere, sollte dies zwar im Logo enthalten sein, aber nicht zu stark integriert sein.
Ich arbeite in einer ländlichen Gegend und das Logo sollte Zuverlässigkeit, Flexibilität und Individualität ausstrahlen und einen hohen Widererkennungswert haben, da es viele andere Schreiner hier gibt. Ich bin bekannt für meine exakte und qualitativ hochwertige Arbeit und bin auch ein Spezialist, wenn es um die Beratung meiner Kunden bei der Fenster und Türenauswahl geht.
Bei den Farben bin ich noch etwas unentschlossen. Derzeit habe ich grau-blau als Farben, bin aber offen für andere Vorschläge. Nur bitte kein rot/rosa. Falls Fragen sind, bitte einfach kurz schreiben.
Besten Dank vorab für die Vorschläge!

```html
<!DOCTYPE html>
<html lang="de">
<head>
<meta charset="utf-8">
<title>KM Wendel – Visitenkarte</title>
<link rel="stylesheet" href="https://fonts.googleapis.com/css2?family=Roboto:wght@400;700&display=swap">
<style>
  :root {
    --stage: #00111a;
    --card: #ffffff;
    --navy: #03005f;
    --ink: #111111;
    --rule: #555555;
  }
  * { margin: 0; padding: 0; box-sizing: border-box; }
  html, body { width: 1200px; height: 817px; overflow: hidden; }
  body {
    background: var(--stage);
    font-family: "Roboto", Arial, sans-serif;
    position: relative;
  }
  .card {
    position: absolute;
    top: 252px;
    width: 483px;
    height: 312px;
    background: var(--card);
    overflow: hidden;
  }
  .card--front { left: 85px; }
  .card--back { left: 632px; }

  .front-brand {
    position: absolute;
    top: 0; left: 0; right: 0;
    height: 271px;
    display: flex;
    align-items: center;
    justify-content: center;
    color: var(--navy);
    font-weight: 700;
    font-size: 50px;
    letter-spacing: 0.5px;
  }
  .service-band {
    position: absolute;
    left: 0; right: 0; bottom: 0;
    height: 41px;
    background: var(--navy);
    color: #fff;
    font-weight: 700;
    font-size: 11.5px;
    display: flex;
    align-items: center;
    justify-content: center;
    letter-spacing: 0.1px;
  }

  .back-bands { position: absolute; inset: 0; }
  .back-initials {
    position: absolute;
    left: 20px; top: 112px;
    width: 140px;
    text-align: center;
    color: var(--navy);
    font-weight: 700;
    font-size: 54px;
    line-height: 1;
  }
  .divider {
    position: absolute;
    left: 185px; top: 48px;
    width: 1px; height: 216px;
    background: var(--rule);
  }
  .contact {
    position: absolute;
    left: 220px; top: 68px;
    color: var(--ink);
    font-size: 15.5px;
    line-height: 18px;
  }
  .contact__name {
    color: var(--navy);
    font-weight: 700;
    font-size: 26px;
    line-height: 30px;
    margin-bottom: 2px;
    margin-left: -2px;
  }
  .contact__block { margin-bottom: 11px; }
  .contact__phones { margin-bottom: 2px; }
  .contact__phones div { display: flex; }
  .contact__label { font-weight: 700; width: 46px; }
  .contact__web { line-height: 16px; }
</style>
</head>
<body>
  <section class="card card--front">
    <div class="front-brand">KM Wendel</div>
    <div class="service-band">FENSTER | TÜREN | ROLLLÄDEN | RAFFSTOREN | INSEKTENSCHUTZ</div>
  </section>

  <section class="card card--back">
    <svg class="back-bands" width="483" height="312" viewBox="0 0 483 312" aria-hidden="true">
      <polygon points="0,0 207,0 180,19 0,19" fill="var(--navy)"/>
      <polygon points="166,312 193,293 483,293 483,312" fill="var(--navy)"/>
    </svg>
    <div class="back-initials">KM</div>
    <div class="divider"></div>
    <div class="contact">
      <div class="contact__name">Ralf Wendel</div>
      <div class="contact__block">
        <div>Lindenweg 14</div>
        <div>79899 Tannbach-Oberried</div>
      </div>
      <div class="contact__phones">
        <div><span class="contact__label">Mobil</span>: 0171 482 56 19</div>
        <div><span class="contact__label">Büro</span>: 07751 638 20 47</div>
        <div><span class="contact__label">Fax</span>: 03212 574 61 08</div>
      </div>
      <div class="contact__web">wendel@email.com</div>
      <div class="contact__web">www.ralf-wendel.de</div>
    </div>
  </section>
</body>
</html>
```